Beer Can Label named: ZAP Ginger Beer

We need a funky design for a Ginger Beer that is made from all natural ingredients. The label needs to be full of Colour, emphasis on the Ginger Root. ZAP (Zested And Poured)

Target Market(s)

None beer drinkers'

Requirements
Must have
• Name on the label must beer easy to read. Needs to be very colourful, playful & even a bit cheaky.
Nice to have
• A label that looks at the benefits of Ginger for the body in a fun artistic design.
Should not have
• Should NOT be a simple, basic, minimalistic design

```html
<!DOCTYPE html>
<html lang="en">
<head>
<meta charset="utf-8">
<title>ZAP Ginger Beer – Can Label</title>
<link rel="stylesheet" href="https://fonts.googleapis.com/css2?family=Sancreek&family=Oswald:wght@600&family=Roboto+Condensed:wght@300&display=swap">
<style>
  :root {
    --backdrop: #d6cfbb;
    --label-dark: #1f1f1f;
    --label-mid: #2c2c2c;
    --cream: #e4d2b4;
    --cream-light: #f7f0e6;
    --ribbon-shade: #b99f83;
    --ribbon-edge: #8a7055;
    --ginger-tan: #c9a57c;
    --leaf-green: #49a83a;
    --type-green: #3aaa48;
    --crown-red: #c4161c;
    --white-type: #f2f2f2;
    --title-shadow: #3a3128;
  }
  html, body {
    margin: 0;
    padding: 0;
    width: 1200px;
    height: 1000px;
    overflow: hidden;
    background: var(--backdrop);
  }
  .canvas {
    position: relative;
    width: 1200px;
    height: 1000px;
  }
  .can-label {
    position: absolute;
    left: 322px;
    top: 50px;
    width: 556px;
    height: 900px;
    display: block;
  }
  .brand-name {
    font-family: "Sancreek", "Georgia", serif;
    fill: var(--cream);
    stroke: var(--title-shadow);
    stroke-width: 3;
    paint-order: stroke;
  }
  .tagline {
    font-family: "Oswald", "Arial Narrow", sans-serif;
    font-weight: 600;
    fill: var(--type-green);
  }
  .label-details {
    font-family: "Roboto Condensed", "Arial Narrow", sans-serif;
    font-weight: 300;
    fill: var(--white-type);
  }
</style>
</head>
<body>
<main class="canvas">
  <svg class="can-label" viewBox="0 0 750 1213" xmlns="http://www.w3.org/2000/svg" aria-labelledby="label-title">
    <title id="label-title">ZAP Ginger Beer can label</title>
    <defs>
      <linearGradient id="board" x1="0" y1="0" x2="1" y2="1">
        <stop offset="0" stop-color="var(--label-mid)"/>
        <stop offset="0.5" stop-color="var(--label-dark)"/>
        <stop offset="1" stop-color="var(--label-mid)"/>
      </linearGradient>
      <radialGradient id="ginger-tones" cx="0.45" cy="0.55" r="0.6">
        <stop offset="0" stop-color="#dcbf98"/>
        <stop offset="0.65" stop-color="var(--ginger-tan)"/>
        <stop offset="1" stop-color="var(--leaf-green)" stop-opacity="0.85"/>
      </radialGradient>
      <path id="frame-shape" d="M83,1100 L83,150 L120,150 Q140,150 150,135 Q160,120 200,122 Q300,128 340,104 Q375,88 410,104 Q450,128 550,122 Q590,120 600,135 Q610,150 630,150 L667,150 L667,1100 L630,1100 Q610,1100 600,1115 Q590,1130 550,1128 Q450,1122 410,1146 Q375,1162 340,1146 Q300,1122 200,1128 Q160,1130 150,1115 Q140,1100 120,1100 Z"/>
      <path id="ribbon-curve" d="M195,914 C310,893 460,926 572,965"/>
    </defs>

    <rect class="label-board" width="750" height="1213" fill="url(#board)"/>

    <g class="label-frame" fill="none" stroke="var(--cream)">
      <use href="#frame-shape" stroke-width="5"/>
      <use href="#frame-shape" stroke-width="2" transform="translate(375 625) scale(0.965 0.978) translate(-375 -625)"/>
    </g>

    <circle class="brand-dot" cx="375" cy="182" r="18" fill="var(--crown-red)"/>

    <g class="title-arrows" stroke="var(--cream)" stroke-width="3" fill="var(--cream)">
      <line x1="248" y1="288" x2="284" y2="288"/>
      <path d="M248,288 l-8,-6 h8 l8,6 l-8,6 h-8 z" stroke="none"/>
      <line x1="466" y1="288" x2="498" y2="288"/>
      <path d="M508,288 l-12,-7 v14 z" stroke="none"/>
    </g>

    <text class="brand-name" x="375" y="344" font-size="140" text-anchor="middle" textLength="160" lengthAdjust="spacingAndGlyphs">ZAP</text>
    <text class="brand-name" x="375" y="454" font-size="132" text-anchor="middle" textLength="480" lengthAdjust="spacingAndGlyphs">GINGER BEER</text>

    <ellipse class="ginger-hero" cx="385" cy="680" rx="225" ry="195" fill="url(#ginger-tones)" role="img" aria-label="Illustration of a fresh ginger root with green leaves"/>

    <g class="tagline-ribbon">
      <path d="M182,940 L125,1010 L230,990 L215,945 Z" fill="var(--ribbon-shade)"/>
      <path d="M578,900 L635,805 L545,845 L560,900 Z" fill="var(--ribbon-shade)"/>
      <path d="M172,862 C300,838 470,868 592,903 L586,988 C470,952 300,925 178,947 Z" fill="var(--cream-light)" stroke="var(--ribbon-edge)" stroke-width="3"/>
      <text class="tagline" font-size="58">
        <textPath href="#ribbon-curve" startOffset="50%" text-anchor="middle" textLength="380" lengthAdjust="spacingAndGlyphs">NATURAL INGREDIENTS</textPath>
      </text>
    </g>

    <g class="label-details" text-anchor="middle">
      <text x="375" y="1016" font-size="26">Zested And Poured</text>
      <text x="375" y="1052" font-size="20">4.2% ALC/VOL.</text>
      <text x="375" y="1074" font-size="12" letter-spacing="6">★★★★★</text>
      <text x="375" y="1102" font-size="20">500mL</text>
    </g>

    <rect class="flourish" x="165" y="1062" width="125" height="18" rx="9" fill="var(--cream)" opacity="0.18" role="img" aria-label="Decorative scroll flourish"/>
    <rect class="flourish" x="460" y="1062" width="125" height="18" rx="9" fill="var(--cream)" opacity="0.18" role="img" aria-label="Decorative scroll flourish"/>
  </svg>
</main>
</body>
</html>
```